Granite Mesa Auto Works web site for repairs,Parts, Accessories and Off Road

Need a wed site design for our light duty truck repair shop, also need to be able to sell our products from this page as well. Has our logo as the headliner and brief description of what we do and our history. An example of what we would want it to work like can be seen at www.kolbysgarage.com . This is a good example of style and accesses ability to buy parts we have.

Reason: needs more time and designs to come in

Target Market(s)

Light duty Diesel truck owners(Varnel,Brisco,Montavel)

Industry/Entity Type

Shop

Number of Pages Required

3 page

Font styles to use
Other font styles liked:
• The same font as our logo

Requirements
Must have
• A little about the shop and all of our services,availability to purchase our products, also a map of where we are located.
Nice to have
• I like the design of www.Kolbysgarage.com. Its easy to use and very descriptive of parts available

```html
<!DOCTYPE html>
<html lang="en">
<head>
<meta charset="utf-8">
<title>Granite Mesa Auto Works</title>
<link href="https://fonts.googleapis.com/css2?family=Raleway:wght@400;500;600;700&family=Open+Sans:wght@400;600;700&display=swap" rel="stylesheet">
<style>
:root{
  --blue:#0f4a86;
  --blue-dark:#0b3563;
  --navy:#0a2544;
  --ink:#333a44;
  --muted:#8a9099;
  --line:#dfe3e8;
  --grey-bg:#eef0f3;
  --white:#ffffff;
  --video-bg:#15191f;
  --btn-grey:#6c737c;
}
*{box-sizing:border-box;margin:0;padding:0}
html,body{width:1200px;height:3024px;overflow:hidden}
body{font-family:"Open Sans",Arial,sans-serif;color:var(--ink);background:var(--white);font-size:14px}
.topbar{height:40px;display:flex;justify-content:space-between;align-items:center;padding:0 48px;font-size:12px;color:var(--muted);border-bottom:1px solid var(--line)}
.topbar .call{display:flex;align-items:center;gap:8px;color:var(--blue)}
.topbar .call small{display:block;font-size:10px;color:var(--muted);line-height:1}
.topbar .call strong{font-size:13px}
.topbar .links{letter-spacing:.5px;font-size:11px}
.header{height:120px;display:flex;justify-content:space-between;align-items:center;padding:0 48px}
.brand{width:248px;height:96px;background:var(--blue-dark);display:flex;align-items:center;justify-content:center;text-align:center;color:var(--white);font-family:"Raleway",sans-serif;font-weight:700;font-size:21px;line-height:1.15;letter-spacing:1px;text-transform:uppercase;padding:0 16px}
.nav{display:flex;height:96px}
.nav a{width:96px;display:flex;align-items:center;justify-content:center;font-family:"Raleway",sans-serif;font-size:13px;font-weight:600;color:var(--blue);text-decoration:none;letter-spacing:.5px}
.nav a.active{background:var(--blue);color:var(--white)}
.hero{height:752px;position:relative;background:linear-gradient(180deg,#5d6b77 0%,#3f4c55 45%,#2f3a33 75%,#3d4a3a 100%)}
.hero h1{position:absolute;left:170px;top:228px;width:960px;font-family:"Raleway",sans-serif;font-weight:500;font-size:58px;line-height:1.15;color:var(--white);text-transform:uppercase;white-space:nowrap}
.dots{position:absolute;right:60px;top:690px;display:flex;gap:8px}
.dots span{width:10px;height:10px;border-radius:50%;background:rgba(255,255,255,.5)}
.dots span.on{background:var(--white)}
.welcome{height:288px;background:var(--grey-bg);text-align:center;padding-top:64px}
.welcome h2{font-family:"Raleway",sans-serif;font-weight:500;font-size:40px;color:var(--blue-dark)}
.welcome p{width:980px;margin:22px auto 0;font-size:12px;line-height:1.6;color:var(--muted)}
.btn{display:inline-block;background:var(--blue-dark);color:var(--white);font-size:11px;font-weight:600;letter-spacing:.5px;padding:9px 22px;text-transform:uppercase}
.welcome .btn{margin-top:28px}
.kits{height:392px;display:flex;gap:48px;padding:32px 48px 0}
.kit{width:336px}
.kit .photo{height:200px}
.kit h3{margin-top:24px;font-family:"Raleway",sans-serif;font-size:15px;font-weight:700;color:var(--blue)}
.kit p{font-size:11px;line-height:1.5;color:var(--muted);margin:6px 0 12px}
.kit .btn{padding:7px 16px}
.shop{height:688px;display:flex;gap:24px;padding:20px 32px 0 40px}
.sidebar{width:264px}
.gear{border:1px solid var(--line)}
.gear h4{margin:24px 0 0;background:var(--blue-dark);color:var(--white);text-align:center;font-family:"Raleway",sans-serif;font-size:15px;font-weight:700;padding:10px 0}
.gear ul{list-style:none;padding:8px 12px}
.gear li{font-size:11.5px;color:var(--muted);padding:7px 0;border-bottom:1px dotted var(--line)}
.gear li::before{content:"› ";color:var(--blue)}
.callbox{margin-top:48px;height:180px;background:var(--blue-dark);color:var(--white);text-align:center;padding-top:44px}
.callbox p{font-family:"Raleway",sans-serif;font-size:26px;font-weight:600}
.callbox strong{display:block;margin-top:12px;font-size:36px;font-weight:700}
.products{flex:1}
.filters{text-align:right;font-size:12px;color:var(--blue);height:36px}
.grid{display:grid;grid-template-columns:repeat(3,1fr);gap:16px}
.card{border:1px solid var(--line);height:290px;padding:12px}
.card .photo{height:120px}
.card h5{margin-top:12px;font-size:12px;font-weight:600;color:var(--blue);height:32px;line-height:1.35}
.card .meta{font-size:11px;color:var(--muted);line-height:1.6;margin-top:6px}
.card .actions{display:flex;gap:8px;margin-top:14px}
.card .actions span{flex:1;text-align:center;font-size:11px;padding:8px 0;color:var(--white)}
.card .view{background:var(--btn-grey)}
.card .add{background:var(--blue-dark)}
.videos{height:500px;background:linear-gradient(180deg,#22282f,var(--video-bg));text-align:center;padding-top:36px}
.videos h2{font-family:"Raleway",sans-serif;font-weight:500;font-size:40px;color:var(--white)}
.video-row{display:flex;justify-content:center;gap:40px;margin-top:20px}
.video{width:424px;height:360px;position:relative;background:linear-gradient(180deg,#5a6068,#2b3036)}
.video .title{position:absolute;left:14px;top:10px;color:var(--white);font-size:16px}
.video .caption{position:absolute;left:0;right:0;bottom:18px;color:var(--white);font-size:17px}
.video svg{position:absolute;left:172px;top:140px}
.footer{height:168px;background:var(--navy);display:flex;justify-content:space-between;align-items:center;padding:0 64px 0 48px}
.contact{font-size:12px;color:#c9d3df;line-height:1.9}
.contact div{display:flex;align-items:center;gap:14px}
.contact b{color:var(--white);font-weight:600;width:70px}
.social{display:flex;gap:22px}
.social span{width:56px;height:56px;border-radius:50%;background:var(--white)}
.copy{height:56px;background:#071a31;color:#8ea0b5;font-size:11px;display:flex;align-items:center;justify-content:center}
</style>
</head>
<body>
<div class="topbar">
  <div class="call">
    <svg width="18" height="18" viewBox="0 0 24 24"><path fill="#0f4a86" d="M6.6 10.8a15 15 0 006.6 6.6l2.2-2.2c.3-.3.7-.4 1-.2 1.1.4 2.3.6 3.6.6.6 0 1 .4 1 1V20c0 .6-.4 1-1 1A17 17 0 013 4c0-.6.4-1 1-1h3.5c.6 0 1 .4 1 1 0 1.3.2 2.5.6 3.6.1.3 0 .7-.2 1z"/></svg>
    <div><small>CALL US</small><strong>1 (555) 014-2290</strong></div>
  </div>
  <div class="links">LOGIN/REGISTER &nbsp;|&nbsp; MY ACCOUNT &nbsp;|&nbsp; CART (0)</div>
</div>
<header class="header">
  <div class="brand">Granite Mesa<br>Auto Works</div>
  <nav class="nav">
    <a class="active">HOME</a><a>ABOUT</a><a>PRODUCT</a><a>SERVICES</a><a>GALLERY</a><a>CONTACT US</a>
  </nav>
</header>
<section class="hero" role="img" aria-label="Photo of a blue diesel semi truck driving on a road in front of trees">
  <h1>Lorem ipsum dolor sit amet,<br>consectetur adipiscing</h1>
  <div class="dots"><span class="on"></span><span></span><span></span></div>
</section>
<section class="welcome">
  <h2>Welcome to Granite Mesa</h2>
  <p>Lorem ipsum dolor sit amet, consectetur adipiscing elit, sed do eiusmod tempor incididunt ut labore et dolore magna aliqua. Ut enim ad minim veniam, quis nostrud exercitation ullamco laboris nisi ut aliquip ex ea commodo consequat. Duis aute irure dolor in reprehenderit in voluptate velit esse cillum dolore eu fugiat nulla pariatur excepteur sint occaecat.</p>
  <span class="btn">Read More</span>
</section>
<section class="kits">
  <div class="kit">
    <div class="photo" role="img" aria-label="Photo of a chrome cold air intake with a red and black filter" style="background:linear-gradient(135deg,#d8dbe0,#8a2c33 55%,#2a2d33)"></div>
    <h3>AIR FILTER KITS</h3>
    <p>Lorem ipsum dolor sit amet, consectetur adipiscing elit sed do eiusmod tempor incididunt ut labore.</p>
    <span class="btn">Read More</span>
  </div>
  <div class="kit">
    <div class="photo" role="img" aria-label="Photo of a transmission rebuild kit with gaskets and parts" style="background:linear-gradient(135deg,#c9b9a4,#8a7560 50%,#4a4038)"></div>
    <h3>TRANSMISSION KITS</h3>
    <p>Lorem ipsum dolor sit amet, consectetur adipiscing elit sed do eiusmod tempor incididunt ut labore.</p>
    <span class="btn">Read More</span>
  </div>
  <div class="kit">
    <div class="photo" role="img" aria-label="Photo of an aluminium intercooler kit with piping" style="background:linear-gradient(135deg,#e2e5e9,#9aa1aa 50%,#4d545d)"></div>
    <h3>INTERCOOLER KITS</h3>
    <p>Lorem ipsum dolor sit amet, consectetur adipiscing elit sed do eiusmod tempor incididunt ut labore.</p>
    <span class="btn">Read More</span>
  </div>
</section>
<section class="shop">
  <aside class="sidebar">
    <div class="gear">
      <h4>KOLBY'S GEAR</h4>
      <ul>
        <li>LED Light Bars &amp; Fog Lights</li>
        <li>Car Care Products</li>
        <li>Fuel &amp; Oil Additives</li>
        <li>Varnel Torqline Series A Parts</li>
        <li>Varnel Torqline Series B Parts</li>
        <li>Varnel Torqline Series C Parts</li>
        <li>Varnel Torqline Series D Parts</li>
        <li>Montavel Dieselon Gen 1 Parts</li>
        <li>Montavel Dieselon Gen 2 Parts</li>
        <li>Montavel Dieselon Gen 3 Parts</li>
        <li>Montavel Dieselon Gen 4 Parts</li>
      </ul>
    </div>
    <div class="callbox"><p>Call Me Now</p><strong>1800 555 0176</strong></div>
  </aside>
  <div class="products">
    <div class="filters">Shop by Brand &nbsp;|&nbsp; Shop by Price &nbsp;|&nbsp; Weekly Deals</div>
    <div class="grid">
      <div class="card"><div class="photo" role="img" aria-label="Photo of a set of valve springs" style="background:linear-gradient(135deg,#f2f2f2,#b5b8bd)"></div><h5>Torqline High Rev Valve Springs</h5><div class="meta">Model: TQ-204 springs<br>Price : $499.00</div><div class="actions"><span class="view">View Details</span><span class="add">Add To Shop</span></div></div>
      <div class="card"><div class="photo" role="img" aria-label="Photo of a handheld engine tuner" style="background:linear-gradient(135deg,#f2f2f2,#3a3f46)"></div><h5>Hallet Mini Pro Tuner (Gen 2)</h5><div class="meta">Model: TQ-204 springs<br>Price : $499.00</div><div class="actions"><span class="view">View Details</span><span class="add">Add To Shop</span></div></div>
      <div class="card"><div class="photo" role="img" aria-label="Photo of a black in-bed fuel tank" style="background:linear-gradient(135deg,#f2f2f2,#23272c)"></div><h5>Varnel Front Fuel Steel Bed 50 Gallon Own Tank</h5><div class="meta">Model: TQ-204 springs<br>Price : $499.00</div><div class="actions"><span class="view">View Details</span><span class="add">Add To Shop</span></div></div>
      <div class="card"><div class="photo" role="img" aria-label="Photo of a set of valve springs" style="background:linear-gradient(135deg,#f2f2f2,#b5b8bd)"></div><h5>Torqline High Rev Valve Springs</h5><div class="meta">Model: TQ-204 springs<br>Price : $499.00</div><div class="actions"><span class="view">View Details</span><span class="add">Add To Shop</span></div></div>
      <div class="card"><div class="photo" role="img" aria-label="Photo of a handheld engine tuner" style="background:linear-gradient(135deg,#f2f2f2,#3a3f46)"></div><h5>Hallet Mini Pro Tuner (Gen 2)</h5><div class="meta">Model: TQ-204 springs<br>Price : $499.00</div><div class="actions"><span class="view">View Details</span><span class="add">Add To Shop</span></div></div>
      <div class="card"><div class="photo" role="img" aria-label="Photo of a black in-bed fuel tank" style="background:linear-gradient(135deg,#f2f2f2,#23272c)"></div><h5>Varnel Front Fuel Steel Bed 50 Gallon Own Tank</h5><div class="meta">Model: TQ-204 springs<br>Price : $499.00</div><div class="actions"><span class="view">View Details</span><span class="add">Add To Shop</span></div></div>
    </div>
  </div>
</section>
<section class="videos">
  <h2>Videos</h2>
  <div class="video-row">
    <div class="video" role="img" aria-label="Video thumbnail of a lifted diesel pickup truck at a truck show">
      <span class="title">Diesel Truck Jam Fall 2013</span>
      <svg width="80" height="80" viewBox="0 0 80 80"><circle cx="40" cy="40" r="38" fill="rgba(0,0,0,.6)"/><path d="M32 24l26 16-26 16z" fill="#fff"/></svg>
      <span class="caption">2013 Kolby's Truck Jam Super Stock Diesel</span>
    </div>
    <div class="video" role="img" aria-label="Video thumbnail of a lifted diesel pickup truck at a truck show">
      <span class="title">Diesel Truck Jam Fall 2013</span>
      <svg width="80" height="80" viewBox="0 0 80 80"><circle cx="40" cy="40" r="38" fill="rgba(0,0,0,.6)"/><path d="M32 24l26 16-26 16z" fill="#fff"/></svg>
      <span class="caption">2013 Kolby's Truck Jam Super Stock Diesel</span>
    </div>
  </div>
</section>
<footer class="footer">
  <div class="contact">
    <div><svg width="14" height="18" viewBox="0 0 14 18"><path d="M7 0a7 7 0 00-7 7c0 5 7 11 7 11s7-6 7-11a7 7 0 00-7-7zm0 9.5A2.5 2.5 0 117 4.5a2.5 2.5 0 010 5z" fill="#fff"/></svg><b>ADDRESS:</b><span>Address Line1, Address Line2<br>Country - 123456</span></div>
    <div><svg width="14" height="14" viewBox="0 0 24 24"><path fill="#fff" d="M6.6 10.8a15 15 0 006.6 6.6l2.2-2.2c.3-.3.7-.4 1-.2 1.1.4 2.3.6 3.6.6.6 0 1 .4 1 1V20c0 .6-.4 1-1 1A17 17 0 013 4c0-.6.4-1 1-1h3.5c.6 0 1 .4 1 1 0 1.3.2 2.5.6 3.6.1.3 0 .7-.2 1z"/></svg><b>FREE CALL:</b><span>1800-555-0139</span></div>
    <div><svg width="14" height="12" viewBox="0 0 14 12"><rect x="0" y="0" width="14" height="12" rx="1" fill="#fff"/><path d="M0 1l7 5 7-5" stroke="#0a2544" stroke-width="1.4" fill="none"/></svg><b>EMAIL ID:</b><span>hello@granitemesaauto.com</span></div>
  </div>
  <div class="social"><span></span><span></span><span></span><span></span></div>
</footer>
<div class="copy">Copyright © 2016 &nbsp;Privacy Policy &nbsp;Terms of use</div>
</body>
</html>
```